Marbrook Chiropractic Center, PLLC sign

I need a design for a sign that will hang from a light post by the road and lets people know that my business is inside the big medical building nearby. I would like it to catch the eye of passing motorists. The design should fit on a sign that is 3 feet wide and 5 feet long. I am a Chiropractor and treat a wide range of patients. I would like the sign to look professional, but eyecatching.

The provided business logo is a .jpg. I can provide .eps if that would be better.
I like the colors in my Marbrook Chiropractic logo.

Marbrook Chiropractic Center, PLLC
(555) 287-4163
www.marbrookspine-example.com
If space allows, please include (listed from most important to least important to include):
• Short Term Care For Your Neck & Back Pain
• No Referral Needed
• Affordable / Insurance Accepted
• Proficient in treating Soft Tissue Problems

Industry/Entity Type

Medical

Requirements
Must have
• logos
website
phone number
Nice to have
• the bullet points
Should not have
• a spine

```html
<!DOCTYPE html>
<html lang="en">
<head>
<meta charset="utf-8">
<title>Marbrook Chiropractic Center, PLLC – Roadside Sign</title>
<link rel="stylesheet" href="https://fonts.googleapis.com/css2?family=Fira+Sans:wght@400;600&display=swap">
<style>
  :root {
    --navy: #283276;
    --ink: #232a78;
    --text: #1c1c1c;
    --white: #ffffff;
    --ribbon-light: #41b4e6;
    --ribbon-dark: #1593d3;
    --accent: #2fa9e0;
  }
  * { margin: 0; padding: 0; box-sizing: border-box; }
  html, body {
    width: 1200px; height: 1000px; overflow: hidden;
    background: var(--navy);
    font-family: "Fira Sans", Arial, sans-serif;
  }
  .canvas { position: relative; width: 1200px; height: 1000px; background: var(--navy); }
  .sign {
    position: absolute; left: 96px; top: 194px;
    width: 1000px; height: 600px;
    background: var(--white);
  }
  .brand-mark {
    position: absolute; left: 0; right: 0; top: 150px;
    display: flex; align-items: center; justify-content: center; gap: 22px;
  }
  .brand-dot {
    width: 34px; height: 34px; border-radius: 50%;
    background: var(--accent);
  }
  .brand-name {
    font-size: 54px; font-weight: 400; color: var(--ink);
    letter-spacing: 1px; line-height: 1;
  }
  .business-name {
    position: absolute; left: 0; right: 0; top: 330px;
    text-align: center; color: var(--ink);
    font-size: 43px; font-weight: 600; line-height: 1;
  }
  .business-name .suffix { font-size: 33px; }
  .contact {
    position: absolute; left: 0; right: 0; top: 400px;
    display: flex; justify-content: center; gap: 44px;
    font-size: 22px; color: var(--text);
  }
  .benefit {
    position: absolute; height: 37px;
    display: flex; align-items: center;
    padding-left: 26px;
    color: var(--white); font-size: 20px; letter-spacing: 0.3px;
    background: linear-gradient(90deg, var(--ribbon-dark), var(--ribbon-light));
    clip-path: polygon(0 0, 100% 0, calc(100% - 10px) 100%, 0 100%);
    text-shadow: 0 1px 1px rgba(0,0,0,0.25);
  }
  .benefit::before { content: "•"; margin-right: 10px; }
  .benefit--care { left: 45px; top: 476px; width: 468px; }
  .benefit--insurance { left: 541px; top: 476px; width: 419px; }
  .benefit--referral { left: 45px; top: 536px; width: 332px; }
  .benefit--tissue { left: 406px; top: 536px; width: 554px; }
</style>
</head>
<body>
<main class="canvas">
  <section class="sign">
    <div class="brand-mark">
      <span class="brand-dot"></span>
      <span class="brand-name">Marbrook Chiropractic</span>
    </div>
    <h1 class="business-name">Marbrook Chiropractic Center, <span class="suffix">PLLC</span></h1>
    <p class="contact">
      <span class="phone">(555) 287-4163</span>
      <span class="web">www.marbrookspine-example.com</span>
    </p>
    <div class="benefit benefit--care">Short Term Care for Neck &amp; Back Pain</div>
    <div class="benefit benefit--insurance">Affordable / Insurance Accepted</div>
    <div class="benefit benefit--referral">No Referral Needed</div>
    <div class="benefit benefit--tissue">Proficient in Treating Soft Tissue Problems</div>
  </section>
</main>
</body>
</html>
```